Post Card Invitation to Wedding Rehearsal Dinner and After Party

This post card should serve as invitations for two events in the wedding weekend for two San Francisco grooms, Derek and Simon.
Each side of the card should have distinct looks and information but tied together with “Before” on the front and “After” on the back.
POST CARD FRONT
Required text:
BEFORE
Derek and Simon’s Wedding: Rehearsal Dinner
Friday, May 22, 2015
5:30 PM
Larkvale Grub Yard
617 Tessler Avenue @ Marlow
San Francisco, CA
Please also convey the following information without necessarily quoting directly: This rehearsal dinner will be held in a private enclosed space in the food truck park. We we will serve beer and wine in our space and provide tickets to purchase food from any of the trucks in the park. Dress is casual.
Look and feel of the card should have a modern, “hipster” feel to it. If you search Google images for “Hipster design” or “hipster infographic” you should get a sense of the overall design and colors. The website for the venue is http://larkvalegrubyard.com/ for reference but please DO NOT use any images or logos from the site.
----------------------
POST CARD REVERSE
Required Text:
AFTER
Derek and Simon’s Wedding: After Party
Saturday, May 23, 2015
7:30 PM
Corvell Harbor Sailing Club
42 Pennick Lane
San Francisco, CA
Please also convey the following information without necessarily quoting directly: Black-tie optional. Dancing, snacks and dessert and cocktails with panoramic views of the San Francisco Bay and Golden Gate Bridge.
This should have a much different look and feel from the front of the card. It should convey an elegant black-tie affair. If you search Google images for “black tie after party invitation” you should get some examples of an overall feel that I am aiming for. The website for the venue is www.chsclub.com but DO NOT use any of the images or logos from the site.
Industry/Entity Type
Wedding
Look and feel
Each slider illustrates characteristics of the customer's brand and the style your logo design should communicate.

```html
<!DOCTYPE html>
<html lang="en">
<head>
<meta charset="utf-8">
<title>Derek &amp; Simon's Wedding – Rehearsal Dinner &amp; After Party</title>
<link rel="stylesheet" href="https://fonts.googleapis.com/css2?family=Lobster&family=Limelight&family=Courgette&family=Josefin+Sans:wght@400;600&family=Roboto+Condensed:wght@700&display=swap">
<style>
  :root {
    --sage: #a9baa4;
    --cream: #f2ebda;
    --coral: #e8524f;
    --coral-dark: #c8403e;
    --maroon: #5b1e1e;
    --ink: #3a1616;
    --phone-green: #bcd8b3;
    --phone-edge: #8fb58a;
    --panel-teal: #3f6b6d;
    --panel-lime: #a9d79b;
    --wine: #7d1f24;
    --wine-deep: #6a1a1e;
    --gold: #d4b27a;
    --parchment: #f1e4c9;
    --tan: #d3b48a;
    --damask-cream: #eee7d6;
    --damask-black: #1b1b1b;
    --white: #ffffff;
  }
  * { margin: 0; padding: 0; box-sizing: border-box; }
  html, body { width: 899px; height: 1200px; overflow: hidden; background: var(--white); }
  .canvas { position: relative; width: 899px; height: 1200px; }
  .abs { position: absolute; }
  .center-text { position: absolute; left: 0; width: 100%; text-align: center; white-space: nowrap; }

  /* Front card */
  .card-front { position: absolute; left: 0; top: 0; width: 899px; height: 581px; background: var(--sage); overflow: hidden; }
  .front-shapes { position: absolute; inset: 0; }
  .speech-text { position: absolute; left: 266px; top: 38px; width: 598px; }
  .couple-title { font-family: 'Lobster', cursive; font-size: 36px; color: var(--cream); top: 12px; }
  .couple-title .amp { color: var(--coral-dark); }
  .couple-title .wedding { color: var(--maroon); }
  .event-title { font-family: 'Limelight', serif; font-size: 35px; letter-spacing: 1px; color: var(--maroon); top: 68px; }
  .event-date { font-family: 'Courgette', cursive; font-size: 25px; color: var(--coral); top: 114px; }
  .event-time { font-family: 'Courgette', cursive; font-size: 36px; color: var(--coral); top: 144px; }
  .venue { font-family: 'Courgette', cursive; font-size: 20px; line-height: 26px; color: var(--ink); top: 200px; }
  .heart-label { font-family: 'Courgette', cursive; font-size: 15px; color: var(--cream); text-align: center; width: 84px; }

  .info-panel { position: absolute; left: 30px; top: 182px; width: 192px; text-align: center; font-family: 'Courgette', cursive; color: var(--cream); }
  .info-panel p { font-size: 16px; line-height: 30px; }
  .info-panel .perks { color: var(--panel-lime); margin-top: 8px; }
  .dress { font-family: 'Roboto Condensed', sans-serif; font-size: 21px; line-height: 24px; color: var(--cream); margin-top: 46px; }

  /* Back card */
  .card-back { position: absolute; left: 0; top: 618px; width: 899px; height: 582px; overflow: hidden; background: var(--wine); }
  .damask-left { position: absolute; left: 0; top: 0; width: 306px; height: 582px; background: linear-gradient(160deg, var(--damask-cream), #e2d8c2); }
  .damask-right { position: absolute; left: 596px; top: 0; width: 303px; height: 582px; background: linear-gradient(160deg, #2b2b2b, var(--damask-black)); }
  .band-label { font-family: 'Limelight', serif; font-size: 22px; letter-spacing: 3px; color: var(--gold); top: 24px; }
  .back-shapes { position: absolute; inset: 0; }
  .back-couple { font-family: 'Lobster', cursive; font-size: 31px; color: var(--parchment); top: 88px; }
  .back-couple .wedding { color: var(--gold); }
  .party-title { font-family: 'Limelight', serif; font-size: 43px; color: var(--gold); top: 134px; }
  .party-date { font-family: 'Josefin Sans', sans-serif; font-weight: 600; font-size: 23px; color: var(--parchment); top: 204px; }
  .party-time { font-family: 'Josefin Sans', sans-serif; font-weight: 600; font-size: 36px; color: var(--parchment); top: 228px; }
  .party-venue { font-family: 'Courgette', cursive; font-size: 20px; line-height: 28px; color: var(--gold); top: 286px; }
  .dress-code { font-family: 'Josefin Sans', sans-serif; font-size: 24px; color: var(--wine); top: 416px; }
  .dress-code strong { font-weight: 600; }
  .party-details { font-family: 'Courgette', cursive; font-size: 14.5px; line-height: 25px; color: var(--ink); top: 448px; }
</style>
</head>
<body>
<main class="canvas">

  <section class="card-front" aria-label="Rehearsal dinner invitation">
    <svg class="front-shapes" width="899" height="581" viewBox="0 0 899 581">
      <!-- phone body and info panel -->
      <rect x="18" y="170" width="216" height="346" rx="14" fill="var(--phone-green)" stroke="var(--phone-edge)" stroke-width="3"/>
      <rect x="30" y="182" width="192" height="304" rx="6" fill="var(--panel-teal)"/>
      <!-- speech bubble -->
      <path d="M266 38 H864 V324 H320 L300 270 L162 162 L266 190 Z" fill="var(--cream)"/>
      <!-- banner and flag -->
      <rect x="266" y="38" width="516" height="58" fill="var(--coral)"/>
      <path d="M806 18 H864 L846 45 L864 72 H806 Z" fill="var(--coral-dark)"/>
      <!-- hearts -->
      <path d="M330 270 C290 240 288 205 308 200 C322 196 330 208 330 214 C330 208 338 196 352 200 C372 205 370 240 330 270 Z" fill="var(--coral)" transform="translate(-33,-26) scale(1.1)"/>
      <path d="M768 270 C728 240 726 205 746 200 C760 196 768 208 768 214 C768 208 776 196 790 200 C810 205 808 240 768 270 Z" fill="var(--coral)" transform="translate(-77,-26) scale(1.1)"/>
    </svg>

    <div class="abs" role="img" aria-label="Illustration of a bearded hipster in a fedora" style="left:78px;top:18px;width:84px;height:162px;background:linear-gradient(#222,#111);border-radius:40px 40px 30px 30px;opacity:.9"></div>
    <div class="abs" role="img" aria-label="Faint dove silhouette" style="left:236px;top:320px;width:110px;height:80px;background:#b9c8b4;border-radius:40px"></div>
    <div class="abs" role="img" aria-label="Illustration of a tandem bicycle trailing tin cans, with headphone cable" style="left:408px;top:330px;width:462px;height:186px;background:linear-gradient(90deg,rgba(122,30,35,.25),rgba(122,30,35,.45));border-radius:20px"></div>

    <div class="speech-text">
      <h1 class="center-text couple-title">Derek <span class="amp">&amp;</span> Simon's <span class="wedding">Wedding</span></h1>
      <h2 class="center-text event-title">REHEARSAL DINNER</h2>
      <p class="center-text event-date">Friday, May 22, 2015</p>
      <p class="center-text event-time">5:30 PM</p>
      <address class="center-text venue" style="font-style:normal">Larkvale Grub Yard<br>617 Tessler Avenue @ Marlow<br>San Francisco, CA</address>
    </div>
    <span class="abs heart-label" style="left:288px;top:220px">BEFORE</span>
    <span class="abs heart-label" style="left:726px;top:220px">BEFORE</span>

    <div class="info-panel">
      <p style="margin-top:18px">This rehearsal dinner will be held in a private enclosed space in the food truck park.</p>
      <p class="perks">Beer, Wine and Tickets available.</p>
      <div class="abs" role="img" aria-label="Sunglasses icon" style="left:64px;top:216px;width:64px;height:20px;background:#111;border-radius:4px 4px 12px 12px"></div>
      <p class="dress">DRESS IS:<br>CASUAL</p>
    </div>
  </section>

  <section class="card-back" aria-label="After party invitation">
    <div class="damask-left" role="img" aria-label="Cream damask pattern"></div>
    <div class="damask-right" role="img" aria-label="Black damask pattern"></div>
    <p class="center-text band-label">AFTER AFTER</p>
    <svg class="back-shapes" width="899" height="582" viewBox="0 0 899 582">
      <rect x="108" y="62" width="684" height="376" rx="60" fill="var(--wine)" stroke="var(--parchment)" stroke-width="3"/>
      <rect x="120" y="74" width="660" height="352" rx="50" fill="none" stroke="var(--gold)" stroke-width="2" stroke-dasharray="8 6"/>
      <rect x="198" y="384" width="504" height="120" rx="48" fill="var(--tan)" stroke="var(--parchment)" stroke-width="3"/>
      <rect x="208" y="394" width="484" height="100" rx="40" fill="none" stroke="var(--wine)" stroke-width="2" stroke-dasharray="7 5"/>
      <path d="M256 408 h8 l-2 6 l4 18 l-6 6 l-6 -6 l4 -18 Z" fill="var(--wine)"/>
      <path d="M636 408 h8 l-2 6 l4 18 l-6 6 l-6 -6 l4 -18 Z" fill="var(--wine)"/>
    </svg>
    <div class="abs" role="img" aria-label="Line drawing of a diamond" style="left:142px;top:64px;width:50px;height:50px;background:var(--wine-deep);border-radius:6px"></div>
    <div class="abs" role="img" aria-label="Gold line drawing of a diamond" style="left:702px;top:64px;width:54px;height:50px;background:var(--gold);opacity:.8;border-radius:6px"></div>
    <div class="abs" role="img" aria-label="Champagne flute with red wine bubbles" style="left:42px;top:324px;width:60px;height:228px;background:linear-gradient(#8a2a2e,#c7a98f);opacity:.7;border-radius:20px 20px 6px 6px"></div>
    <div class="abs" role="img" aria-label="Champagne flute with sparkling wine" style="left:816px;top:324px;width:56px;height:228px;background:linear-gradient(#e9e3d3,#8c8a84);opacity:.7;border-radius:20px 20px 6px 6px"></div>

    <h1 class="center-text back-couple">Derek <span class="wedding">&amp;</span> Simon's <span class="wedding">Wedding</span></h1>
    <h2 class="center-text party-title">AFTER PARTY</h2>
    <p class="center-text party-date">SATURDAY, MAY 23, 2015</p>
    <p class="center-text party-time">7:30 PM</p>
    <address class="center-text party-venue">Corvell Harbor Sailing Club<br>42 Pennick Lane<br>San Francisco, CA</address>
    <p class="center-text dress-code">BLACK-TIE <strong>OPTIONAL.</strong></p>
    <p class="center-text party-details">Dancing, snacks and dessert and cocktails with panoramic<br>views of the San Francisco Bay and Golden Gate Bridge.</p>
  </section>

</main>
</body>
</html>
```